Design Large Inspirational Artwork with Long Quote

Design a large piece of art with a quote from Marcus Hallwell.

QUOTE
"The thing that's so interesting about being alive is that you're all in. No matter what you do, you're all in. This is gonna kill you, so I think you might as well play the most magnificent game you can while you're waiting. Because, do you have anything better to do? Why not pick the best thing possible that you could do? Because you're more powerful than you think, way more powerful than you think. I mean, God only knows what you are in the final analysis. You're blind to your own weaknesses, but you're also blind to your own strengths. How far could you take that if you stopped wasting time, and if you stopped lying, and if you oriented yourself to the highest possible good that you could conceive of and you committed to that? How much good could you do? Well, I would say: why don't you find out?"

SIZE
A high-resolution print size of 6' wide and 3' tall should provide ample space for both the quote and the accompanying artwork.

TYPOGRAPHY
Choose a bold, clean, and easily readable font for the quote. You could also experiment with different font sizes for certain words or phrases to emphasize their importance within the quote.

COLORS
Since the quote is thought-provoking and reflective, you might want to use a color palette that evokes a sense of introspection and depth. Consider using cool, calming colors like shades of blue, gray, or green. Alternatively, you can use a contrasting color scheme with a light background and dark text to make the quote stand out.

ARTWORK
Select / create / edit background artwork to complement the quote.
While a great design might be minimalistic and/or greyscale, I'd really like to see some full color options. This might be anything from photography or graphics inspired by the ideas in the text, to abstract colors or illustrations that feel like the sentiment expressed.
The art should capture your attention and encourage you to read the text. The art should be visually appealing, both at a distance and up close, regardless of whether the text is read.
Updates

Having trouble confirming the exact print size.

Still looking for printing solution and final size confirmation.

Target Market(s)

Personal, business, office

Industry/Entity Type

None

Font styles to use
Sans Serif
Script

Requirements
Must have
• Entire quote, legible text, modern design, attractive artwork, approx 6ft wide and 3ft tall
Nice to have
• Different font (sizes) for certain words or phrases to emphasize their importance within the quote.

```html
<!DOCTYPE html>
<html lang="en">
<head>
<meta charset="utf-8">
<title>Why Don't You Find Out — Quote Artwork</title>
<link rel="stylesheet" href="https://fonts.googleapis.com/css2?family=Arvo:wght@400;700&family=Zilla+Slab:wght@300;400;700&family=Didact+Gothic&display=swap">
<style>
  :root {
    --sky-deep: #3b6ea6;
    --sky-mid: #6fa6c8;
    --sky-light: #d6eaf2;
    --mist: #eef7f9;
    --panel: rgba(255, 255, 255, 0.32);
    --white: #ffffff;
    --navy: #0e0e6a;
    --slate: #3e6b9c;
    --periwinkle: #6a6cf2;
    --forest: #0b6a3a;
    --aqua: #8ff4f2;
  }
  * { margin: 0; padding: 0; box-sizing: border-box; }
  html, body { width: 1200px; height: 600px; overflow: hidden; }
  body { position: relative; }

  .backdrop {
    position: absolute; inset: 0;
    background:
      radial-gradient(ellipse 420px 320px at 1080px 120px, rgba(255,255,255,0.85), rgba(255,255,255,0) 70%),
      radial-gradient(ellipse 380px 260px at 1120px 520px, rgba(60,90,110,0.45), rgba(60,90,110,0) 70%),
      linear-gradient(90deg, var(--sky-deep) 0%, var(--sky-deep) 18%, var(--sky-mid) 50%, var(--sky-light) 80%, var(--mist) 100%);
  }

  .quote-panel {
    position: absolute; left: 61px; top: 58px; width: 1006px; height: 478px;
    background: var(--panel); border-radius: 14px;
  }

  .artwork { position: absolute; inset: 0; }

  .slab { font-family: "Arvo", "Zilla Slab", Georgia, serif; font-weight: 700; }
  .slab-light { font-family: "Zilla Slab", Georgia, serif; font-weight: 300; }
  .thin { font-family: "Didact Gothic", Arial, sans-serif; font-weight: 400; }
  .mark { font-family: "Arvo", Georgia, serif; font-weight: 700; }

  .c-white { fill: var(--white); }
  .c-navy { fill: var(--navy); }
  .c-slate { fill: var(--slate); }
  .c-peri { fill: var(--periwinkle); }
  .c-forest { fill: var(--forest); }
  .c-aqua { fill: var(--aqua); }
  .stroke-white { fill: none; stroke: var(--white); stroke-width: 3.5; }
</style>
</head>
<body>
  <div class="backdrop" role="img" aria-label="Misty blue sky over mountain peaks with silhouetted people raising their arms in triumph on a summit"></div>
  <div class="quote-panel"></div>

  <svg class="artwork" width="1200" height="600" viewBox="0 0 1200 600">
    <text class="mark c-white" x="66" y="112" font-size="92">&ldquo;</text>

    <g class="speech-tail">
      <polyline class="stroke-white" points="850,536.5 876,536.5 876,577 913,536.5 1001,536.5"/>
      <text class="mark c-white" x="1003" y="574" font-size="62">&rdquo;</text>
      <path class="stroke-white" d="M1067,489 V526 Q1067,536 1057,536 H1052"/>
    </g>

    <g class="quote" lengthAdjust="spacingAndGlyphs">
      <text class="slab c-white" x="105" y="109.5" font-size="18" textLength="351" lengthAdjust="spacingAndGlyphs">The thing that's so interesting about</text>
      <text class="slab c-white" x="468" y="109.5" font-size="20" textLength="117" lengthAdjust="spacingAndGlyphs">being alive</text>
      <text class="slab c-white" x="594" y="109.5" font-size="16" textLength="178" lengthAdjust="spacingAndGlyphs" opacity="0.9">is that you're all in.</text>
      <text class="slab c-navy" x="778" y="109.5" font-size="19" textLength="247" lengthAdjust="spacingAndGlyphs">No matter what you do,</text>

      <text class="slab c-navy" x="105" y="148" font-size="29" textLength="173" lengthAdjust="spacingAndGlyphs">you're all in.</text>
      <text class="thin c-slate" x="303" y="148" font-size="32" textLength="209" lengthAdjust="spacingAndGlyphs">This is gonna</text>
      <text class="slab c-slate" x="523" y="148" font-size="32" textLength="129" lengthAdjust="spacingAndGlyphs">kill you,</text>
      <text class="slab c-navy" x="661" y="146" font-size="15" textLength="358" lengthAdjust="spacingAndGlyphs">so I think you might as well play the most</text>

      <text class="slab c-navy" x="105" y="180" font-size="16" textLength="413" lengthAdjust="spacingAndGlyphs">magnificent game you can while you're waiting.</text>
      <text class="slab c-peri" x="530" y="181" font-size="21" textLength="491" lengthAdjust="spacingAndGlyphs">Because, do you have anything better to do?</text>

      <text class="slab c-slate" x="105" y="218" font-size="23" textLength="685" lengthAdjust="spacingAndGlyphs">Why not pick the best thing possible that you could do?</text>
      <text class="slab c-forest" x="805" y="218" font-size="27" textLength="220" lengthAdjust="spacingAndGlyphs">Because you're</text>

      <text class="slab c-forest" x="105" y="255" font-size="28" textLength="920" lengthAdjust="spacingAndGlyphs">more powerful than you think, way more powerful than you think</text>

      <text class="slab c-navy" x="105" y="289" font-size="20" textLength="920" lengthAdjust="spacingAndGlyphs">I mean, God only knows what you are in the final analysis.  You're blind to your own</text>

      <text class="slab c-navy" x="105" y="325" font-size="30" textLength="173" lengthAdjust="spacingAndGlyphs">weaknesses,</text>
      <text class="slab c-peri" x="297" y="325" font-size="34" textLength="731" lengthAdjust="spacingAndGlyphs">but you're also blind to your own strengths.</text>

      <text class="slab-light c-navy" x="105" y="361" font-size="23" textLength="920" lengthAdjust="spacingAndGlyphs">How far could you take that if you stopped wasting time, and if you stopped lying,</text>

      <text class="slab c-forest" x="105" y="396" font-size="18" textLength="917" lengthAdjust="spacingAndGlyphs">and if you oriented yourself to the highest possible good that you could conceive of and</text>

      <text class="slab c-navy" x="105" y="438" font-size="34" textLength="920" lengthAdjust="spacingAndGlyphs">you committed to that? How much good could you do?</text>

      <text class="slab c-aqua" x="105" y="489" font-size="32" textLength="316" lengthAdjust="spacingAndGlyphs">Well, I would say:</text>
      <text class="slab c-aqua" x="440" y="489" font-size="48" textLength="585" lengthAdjust="spacingAndGlyphs">why don't you find out?</text>
    </g>
  </svg>
</body>
</html>
```